Design a Professional Business Card for Vello Marra

Design a business card for Vello Marra, we are a National Sport Court Company.

West Region Address: 4172 Glen Harrow Ct, Suite #210 Englewood, Colorado 80112
East Region Address: 7316 38th Ave W, Bradenton, Florida 34210

Target Market(s)

High End Residential & Institutional Clients

Industry/Entity Type

Design & Construction

Contact Information for Business Card

Logo/Brand/Colors/ name, number (provided in comments)

Requirements
Must have
• Colors only provided in logo
Should not have
• Any other colors not in existing logo (attached)

```html
<!DOCTYPE html>
<html lang="en">
<head>
<meta charset="utf-8">
<title>Vello Marra – Business Card</title>
<link href="https://fonts.googleapis.com/css2?family=Roboto:wght@400;500;700&display=swap" rel="stylesheet">
<style>
  :root {
    --navy: #1f3563;
    --green: #046a38;
    --white: #ffffff;
    --stage: #3a3a3a;
  }
  * { box-sizing: border-box; margin: 0; padding: 0; }
  html, body { width: 1200px; height: 694px; overflow: hidden; }
  body {
    background: var(--stage);
    font-family: "Roboto", sans-serif;
    display: flex;
    align-items: center;
    justify-content: space-between;
    padding: 0 40px;
  }
  .card {
    width: 540px;
    height: 309px;
    border-radius: 22px;
    overflow: hidden;
    position: relative;
  }

  /* Front */
  .card-front {
    background: var(--navy);
    color: var(--white);
    display: flex;
    flex-direction: column;
    align-items: center;
    justify-content: center;
    gap: 26px;
  }
  .brand {
    display: flex;
    align-items: center;
    gap: 18px;
  }
  .brand-dot {
    border-radius: 50%;
    background: var(--green);
    flex: none;
  }
  .brand-name {
    font-weight: 700;
    text-transform: uppercase;
    letter-spacing: 0.06em;
    line-height: 1;
  }
  .card-front .brand-dot { width: 70px; height: 70px; }
  .card-front .brand-name { font-size: 46px; color: var(--white); }
  .tagline { font-size: 17px; font-weight: 700; letter-spacing: 0.01em; }

  /* Back */
  .card-back { background: var(--white); }
  .back-top {
    height: 218px;
    display: flex;
    align-items: center;
    padding: 0 24px 0 26px;
  }
  .card-back .brand { gap: 12px; width: 218px; }
  .card-back .brand-dot { width: 44px; height: 44px; }
  .card-back .brand-name { font-size: 25px; color: var(--navy); }
  .divider {
    width: 1.5px;
    height: 140px;
    background: var(--green);
    margin: 0 22px 0 14px;
  }
  .contact { color: var(--navy); }
  .person-name { font-size: 20px; font-weight: 700; }
  .person-title { font-size: 13px; margin: 2px 0 10px; }
  .contact-list { list-style: none; font-size: 13px; line-height: 1.65; }
  .contact-list li { display: flex; align-items: center; gap: 8px; }
  .contact-list svg { width: 12px; height: 12px; fill: var(--green); flex: none; }
  .contact-list .no-icon { padding-left: 20px; }

  .back-band {
    position: absolute;
    left: 0; right: 0; bottom: 0;
    height: 91px;
    background: var(--navy);
    border-top: 3px solid var(--white);
    box-shadow: 0 -3px 0 var(--green);
    display: flex;
    justify-content: space-between;
    align-items: center;
    padding: 0 26px;
    color: var(--white);
    font-size: 12.5px;
    line-height: 1.45;
  }
  .address { width: 235px; }
  .address-east { text-align: right; }
</style>
</head>
<body>
  <section class="card card-front">
    <div class="brand">
      <span class="brand-dot"></span>
      <span class="brand-name">Vello Marra</span>
    </div>
    <p class="tagline">We are a National Sport Court Company</p>
  </section>

  <section class="card card-back">
    <div class="back-top">
      <div class="brand">
        <span class="brand-dot"></span>
        <span class="brand-name">Vello Marra</span>
      </div>
      <span class="divider"></span>
      <div class="contact">
        <p class="person-name">Dorian L. Whitcomb, ASLA</p>
        <p class="person-title">CEO &amp; Founder</p>
        <ul class="contact-list">
          <li class="no-icon">(303) 555-0147</li>
          <li>
            <svg viewBox="0 0 24 24" aria-hidden="true"><path d="M6.6 10.8a15.1 15.1 0 006.6 6.6l2.2-2.2c.3-.3.7-.4 1-.2 1.1.4 2.3.6 3.6.6.6 0 1 .4 1 1V20c0 .6-.4 1-1 1A17 17 0 013 4c0-.6.4-1 1-1h3.5c.6 0 1 .4 1 1 0 1.3.2 2.5.6 3.6.1.3 0 .7-.2 1z"/></svg>
            1-800-555-0193
          </li>
          <li>
            <svg viewBox="0 0 24 24" aria-hidden="true"><path d="M2 5h20v14H2z M2 5l10 8 10-8" fill="none" stroke="#046a38" stroke-width="2.4"/></svg>
            dorian@vellomarraco.com
          </li>
          <li>
            <svg viewBox="0 0 24 24" aria-hidden="true"><circle cx="12" cy="12" r="9" fill="none" stroke="#046a38" stroke-width="2.4"/><path d="M3 12h18M12 3c3 3 3 15 0 18M12 3c-3 3-3 15 0 18" fill="none" stroke="#046a38" stroke-width="1.8"/></svg>
            www.vellomarra.com
          </li>
        </ul>
      </div>
    </div>
    <div class="back-band">
      <p class="address address-west">West Region Address:<br>4172 Glen Harrow Ct, Suite #210<br>Englewood, Colorado 80112</p>
      <p class="address address-east">East Region Address:<br>7316 38th Ave W, Bradenton,<br>Florida 34210</p>
    </div>
  </section>
</body>
</html>
```